Business Card for a Life Coaching Company

BRAVOPEAK is a Life Coaching company that was initiated to support people who want to transform thier life or ana aspect of it.
our slogan is : "Dream. Believe. Succeed"
our logo is uploaded.
The name of the company implies that leadership, strength and wisdom required to change your life.
We want an attractive business card that would give an impression of reliability, support and change. so we really want it unique. Here are some examples of unique cards:

http://www.cardcraftvault.example/2009/05/100-really-creative-business-cards/

BravoPeak is a life coaching organization focusing on individual transformation through the application of relevant and timeless principles of success.  BravoPeak believes that real, sustainable life transformations are brought about by tuning into the timeless wisdom we each carry in our hearts while boldy acting in the direction of our dreams.

Contacts on the card:
Address: 7 Tarek Nour El Dine Heliopolis Cairo Egypt
Tel: +202 24 71 38 52
Fax: +202 24 71 38 17
Mobile: +2 012 684 2097 (Dalia Soliman)
+2 0199915815 (Tariq Bhatti)

By the way, our temporary website is http://www.bravopeak.example

We have attached an .eps file with various configurations of our logo.

```html
<!DOCTYPE html>
<html lang="en">
<head>
<meta charset="utf-8">
<title>BravoPeak Business Card</title>
<link href="https://fonts.googleapis.com/css2?family=Cinzel:wght@400&family=Josefin+Sans:wght@400&display=swap" rel="stylesheet">
<style>
  :root {
    --page: #ffffff;
    --card-top: #ffffff;
    --card-bottom: #8e8e8e;
    --ink: #1a1a1a;
    --logo-grey: #8c8c8c;
    --accent: #ef6a1f;
    --accent-deep: #e4471c;
    --accent-light: #f5892b;
    --crop: #9a9a9a;
    --figure-dark: #1c1c1c;
  }
  * { margin: 0; padding: 0; box-sizing: border-box; }
  html, body {
    width: 1200px; height: 900px; overflow: hidden;
    background: var(--page);
  }
  .sheet { position: relative; width: 1200px; height: 900px; }

  .card {
    position: absolute; top: 196px; width: 350px; height: 518px;
    overflow: hidden;
  }
  .card--front {
    left: 230px;
    background: radial-gradient(ellipse 90% 70% at 50% 30%, var(--card-top) 0%, #e8e8e8 55%, var(--card-bottom) 100%);
  }
  .card--back {
    left: 628px;
    border: 1px solid #d0d0d0;
    background: linear-gradient(180deg, var(--card-top) 0%, #f6f6f6 55%, #cfcfcf 100%);
  }

  .crop-marks { position: absolute; inset: 0; pointer-events: none; }

  /* Front */
  .brand {
    position: absolute; top: 60px; left: 52px;
    display: flex; align-items: center; gap: 16px;
  }
  .brand__square { width: 52px; height: 52px; background: var(--accent); flex: none; }
  .brand__name {
    font-family: "Cinzel", serif; font-weight: 400;
    font-size: 50px; line-height: 0.98; color: var(--logo-grey);
    letter-spacing: -1px;
  }
  .front-figures {
    position: absolute; left: 80px; top: 176px; width: 200px; height: 270px;
  }
  .slogan {
    position: absolute; left: 0; right: 0; top: 458px;
    text-align: center; font-family: "Cinzel", serif;
    font-size: 20px; letter-spacing: 0.3px; color: #ffffff;
  }

  /* Back */
  .contact-row { position: absolute; left: 0; right: 0; height: 26px; }
  .contact-row__label {
    position: absolute; top: 6px;
    font-family: "Josefin Sans", sans-serif; font-size: 12px; color: var(--ink);
    text-align: right; white-space: nowrap;
  }
  .contact-row__pill {
    position: absolute; right: -2px; top: 0; height: 24px;
    border-radius: 12px 0 0 12px;
    background: linear-gradient(90deg, var(--accent-light), var(--accent));
    font-family: "Josefin Sans", sans-serif; font-size: 12px; color: #ffffff;
    padding: 7px 0 0 12px; white-space: nowrap;
  }
  .contact-row__pill--person {
    background: linear-gradient(90deg, var(--accent), var(--accent-deep));
  }
  .back-figures {
    position: absolute; left: 40px; top: 316px; width: 270px; height: 176px;
  }
</style>
</head>
<body>
<main class="sheet">

  <svg class="crop-marks" width="1200" height="900" aria-hidden="true">
    <g stroke="var(--crop)" stroke-width="1">
      <line x1="230" y1="172" x2="230" y2="188"/><line x1="206" y1="196" x2="222" y2="196"/>
      <line x1="580" y1="172" x2="580" y2="188"/><line x1="588" y1="196" x2="604" y2="196"/>
      <line x1="230" y1="722" x2="230" y2="738"/><line x1="206" y1="714" x2="222" y2="714"/>
      <line x1="580" y1="722" x2="580" y2="738"/><line x1="588" y1="714" x2="604" y2="714"/>
      <line x1="628" y1="172" x2="628" y2="188"/><line x1="604" y1="196" x2="620" y2="196"/>
      <line x1="976" y1="172" x2="976" y2="188"/><line x1="984" y1="196" x2="1000" y2="196"/>
      <line x1="628" y1="722" x2="628" y2="738"/><line x1="604" y1="714" x2="620" y2="714"/>
      <line x1="976" y1="722" x2="976" y2="738"/><line x1="984" y1="714" x2="1000" y2="714"/>
    </g>
  </svg>

  <section class="card card--front">
    <div class="brand">
      <span class="brand__square" aria-hidden="true"></span>
      <span class="brand__name">BRAVO<br>PEAK</span>
    </div>
    <svg class="front-figures" role="img" aria-label="Silhouettes of a businessman and a businesswoman standing side by side" viewBox="0 0 200 270">
      <defs>
        <radialGradient id="frontFig" cx="0.5" cy="0.5" r="0.5">
          <stop offset="0" stop-color="var(--figure-dark)" stop-opacity="0.7"/>
          <stop offset="0.6" stop-color="var(--figure-dark)" stop-opacity="0.35"/>
          <stop offset="1" stop-color="var(--figure-dark)" stop-opacity="0"/>
        </radialGradient>
      </defs>
      <ellipse cx="100" cy="135" rx="100" ry="135" fill="url(#frontFig)"/>
    </svg>
    <p class="slogan">DREAM BELIEVE SUCCEED</p>
  </section>

  <section class="card card--back">
    <div class="contact-row" style="top:60px">
      <span class="contact-row__label" style="right:190px">Telephone</span>
      <span class="contact-row__pill" style="left:168px">+202 24 71 38 52</span>
    </div>
    <div class="contact-row" style="top:96px">
      <span class="contact-row__label" style="right:166px">Fax</span>
      <span class="contact-row__pill" style="left:192px">+202 24 71 38 17</span>
    </div>
    <div class="contact-row" style="top:132px">
      <span class="contact-row__label" style="right:246px">Address</span>
      <span class="contact-row__pill" style="left:112px">7 Tarek Nour El Dine Heliopolis</span>
    </div>
    <div class="contact-row" style="top:164px">
      <span class="contact-row__pill" style="left:164px;padding-left:66px">Cairo Egypt</span>
    </div>
    <div class="contact-row" style="top:228px">
      <span class="contact-row__label" style="right:178px">Dalia Soliman</span>
      <span class="contact-row__pill contact-row__pill--person" style="left:182px">+2 012 684 2097</span>
    </div>
    <div class="contact-row" style="top:262px">
      <span class="contact-row__label" style="right:178px">Tariq Bhatti</span>
      <span class="contact-row__pill contact-row__pill--person" style="left:182px">+2 019 732 8406</span>
    </div>
    <svg class="back-figures" role="img" aria-label="Silhouettes of a group of five business people standing in a row" viewBox="0 0 270 176">
      <defs>
        <radialGradient id="backFig" cx="0.5" cy="0.5" r="0.5">
          <stop offset="0" stop-color="var(--figure-dark)" stop-opacity="0.6"/>
          <stop offset="0.6" stop-color="var(--figure-dark)" stop-opacity="0.3"/>
          <stop offset="1" stop-color="var(--figure-dark)" stop-opacity="0"/>
        </radialGradient>
      </defs>
      <ellipse cx="135" cy="88" rx="135" ry="88" fill="url(#backFig)"/>
    </svg>
  </section>

</main>
</body>
</html>
```